Luxury Business Card Design for High-End Window Treatments

Gilded Slatworks
Custom Plantation Shutters & Architectural Shading Systems

⸻

BACK

Daniel Ferrowitz
Owner

Custom Interior & Exterior Window Treatments

919-555-0187
gildedslatworks.example

I have included a picture that I’m hoping we can use on the back, but I’m also wondering if you can get rid of the ladder? Should we get rid of shutters , shades and blinds underneath Gilded Slatworks?

Target Market(s)

High-end residential homeowners, custom home builders, architects, interior designers, and luxury renovation clients seeking premium plantation shutters and motorized architectural shading systems.

Industry/Entity Type

Custom Window treatments

Contact Information for Business Card

Front Gilded Slatworks Custom Plantation Shutters Motorized Architectural Shading Systems BACK Daniel Ferrowitz Owner 919-555-0187 GildedSlatworks.example Custom Interior & Exterior Window Treatments By Appointment

Requirements
Nice to have
• Not 100% sure on nice to halves or the color but you can definitely check out my website to get a better understanding of what I’m trying to do

```html
<!DOCTYPE html>
<html lang="en">
<head>
<meta charset="utf-8">
<title>Gilded Slatworks — Business Card</title>
<link rel="stylesheet" href="https://fonts.googleapis.com/css2?family=Montserrat:wght@400;500;600;700;800&family=Fenix&display=swap">
<style>
  :root {
    --stage: #d7d7d7;
    --card-black: #050505;
    --cream: #ece6da;
    --gold: #f2c94c;
    --gold-deep: #b8891c;
    --gold-light: #ffd867;
    --ink: #141006;
    --sky: #4f86d6;
    --foliage: #4a5a3a;
    --house-shadow: #1f2326;
  }
  * { margin: 0; padding: 0; box-sizing: border-box; }
  html, body {
    width: 906px; height: 1200px; overflow: hidden;
    background: var(--stage);
    font-family: "Montserrat", sans-serif;
  }
  .sheet { position: relative; width: 906px; height: 1200px; }

  .card {
    position: absolute; left: 73px; width: 760px; height: 456px;
    background: var(--card-black); overflow: hidden;
    box-shadow: 14px 16px 22px rgba(0,0,0,0.28);
  }
  .card--front { top: 112px; }
  .card--back { top: 636px; }

  /* Front */
  .front__brand {
    position: absolute; top: 78px; left: 0; right: 0; text-align: center;
    color: var(--cream); font-weight: 400; font-size: 62px; line-height: 1.05;
    letter-spacing: 0.5px;
  }
  .front__services {
    position: absolute; top: 222px; left: 0; right: 0; text-align: center;
    font-family: "Fenix", serif; color: var(--gold); font-size: 25px; word-spacing: 12px;
  }
  .front__band {
    position: absolute; top: 282px; left: 50px; width: 690px; height: 95px;
    background: linear-gradient(90deg, rgba(184,137,28,0) 0%, var(--gold-deep) 18%, var(--gold-light) 55%, var(--gold) 80%, rgba(184,137,28,0) 100%);
    display: flex; align-items: center; justify-content: center; text-align: center;
  }
  .front__tagline {
    width: 440px; color: var(--ink); font-weight: 500; font-size: 18px; line-height: 1.3;
  }

  /* Back */
  .back__photo {
    position: absolute; top: 0; right: 0; width: 433px; height: 456px;
    background:
      linear-gradient(90deg, var(--card-black) 0%, rgba(5,5,5,0) 22%),
      linear-gradient(180deg, var(--sky) 0%, #8fb3e0 26%, #cfd3d0 34%, var(--house-shadow) 48%, #2c3234 72%, var(--foliage) 86%, #7b7a6c 100%);
  }
  .back__brand {
    position: absolute; top: 64px; left: 0; width: 327px; text-align: center;
    color: var(--cream); font-weight: 400; font-size: 34px; line-height: 1.08;
  }
  .back__services {
    position: absolute; top: 152px; left: 0; width: 327px; text-align: center;
    font-family: "Fenix", serif; color: var(--gold); font-size: 14px; word-spacing: 6px;
  }
  .back__person { position: absolute; top: 198px; left: 68px; padding-left: 27px; }
  .back__person::before {
    content: ""; position: absolute; left: 0; top: 4px; width: 6px; height: 40px; background: var(--gold);
  }
  .back__name { color: #fff; font-weight: 600; font-size: 25px; line-height: 1.1; }
  .back__role { color: var(--cream); font-size: 14px; }
  .back__contacts { position: absolute; top: 278px; left: 68px; list-style: none; }
  .back__contact {
    display: flex; align-items: center; gap: 16px;
    color: #fff; font-size: 19px; height: 30px;
  }
  .back__contact svg { width: 18px; height: 18px; }
  .back__band {
    position: absolute; top: 358px; left: 45px; width: 715px; height: 48px;
    background: linear-gradient(90deg, rgba(184,137,28,0) 0%, var(--gold-deep) 14%, var(--gold-light) 52%, var(--gold) 82%, rgba(242,201,76,0.15) 100%);
    display: flex; align-items: center; justify-content: center;
  }
  .back__slogan { color: var(--ink); font-weight: 700; font-size: 17px; padding-left: 40px; }
</style>
</head>
<body>
<main class="sheet">
  <section class="card card--front" aria-label="Card front">
    <h1 class="front__brand">Gilded<br>Slatworks</h1>
    <p class="front__services">Shutters Shades Blinds</p>
    <div class="front__band">
      <p class="front__tagline">Gilded Slatworks Custom Plantation Shutters Motorized Architectural Shading Systems</p>
    </div>
  </section>

  <section class="card card--back" aria-label="Card back">
    <div class="back__photo" role="img" aria-label="Photo of a luxury home exterior with screened porch, pine trees and blue sky"></div>
    <h2 class="back__brand">Gilded<br>Slatworks</h2>
    <p class="back__services">Shutters Shades Blinds</p>
    <div class="back__person">
      <p class="back__name">Daniel Ferrowitz</p>
      <p class="back__role">Owner</p>
    </div>
    <ul class="back__contacts">
      <li class="back__contact">
        <svg viewBox="0 0 24 24" aria-hidden="true"><path fill="#f2c94c" d="M6.6 10.8a15.1 15.1 0 0 0 6.6 6.6l2.2-2.2a1 1 0 0 1 1-.25 11.4 11.4 0 0 0 3.6.57 1 1 0 0 1 1 1V20a1 1 0 0 1-1 1A17 17 0 0 1 3 4a1 1 0 0 1 1-1h3.5a1 1 0 0 1 1 1c0 1.25.2 2.45.57 3.57a1 1 0 0 1-.25 1z"/></svg>
        <span>919-555-0187</span>
      </li>
      <li class="back__contact">
        <svg viewBox="0 0 24 24" aria-hidden="true"><circle cx="12" cy="12" r="10" fill="#f2c94c"/><path d="M2 12h20M12 2c3 3 3 17 0 20M12 2c-3 3-3 17 0 20" stroke="#050505" stroke-width="1.4" fill="none"/></svg>
        <span>gildedslatworks.example</span>
      </li>
    </ul>
    <div class="back__band">
      <p class="back__slogan">Custom Interior &amp; Exterior Window Treatments</p>
    </div>
  </section>
</main>
</body>
</html>
```